CD-/Plattencover für Musikalbum
Zielgruppe
Wir sind eine Tonträgerfirma und bewegen uns im Low-Budget-Segment.
Aufgabenstellung
Artwork-Design (Cover) für ein Musikalbum : „Sommerpfauenfest”
Wir benötigen nicht das komplette Artwork, sondern ein Frontcover
(121 x 120 mm + 20 mm Beschnitt) wg. etwaiger Verschiebung der Positionierung.
Fertigstellung (Aufziehen des Inlays und Labels) erfolgt später bei uns im Hause.
Wir benötigen später eine offene psd-Datei mit allen Ebenen.
Wichtig: Schriften nicht gerastert ggfs. Schrift mitliefern.
Was wir uns vorstellen:
- Entsprechend der Musik Bild, Tracks Beispiele:
Bis zum letzten Leuchtturm
Eine Rose, die nach Morgen duftet
Ganz viel Sonnenschein
Der Sommer bleibt Gold
Egon, wir tanzen bis Mainz
- Bildmaterial sollte bei pixelkammer, bildarena oder o-frame ausgesucht werden, das Bildmaterial wird dann später auch von uns dort eingekauft.
- keine Künstlerfotos.

```html
<!DOCTYPE html>
<html lang="de">
<head>
<meta charset="utf-8">
<title>Sommerpfauenfest – Frontcover</title>
<link rel="stylesheet" href="https://fonts.googleapis.com/css2?family=Titan+One&family=Open+Sans:wght@700&display=swap">
<style>
  :root {
    --title-blue: #1b8fd2;
    --title-shadow: #3a302e;
    --track-ink: #1e1a1a;
    --disc-white: #ffffff;
    --light-blue: #2f7fe0;
    --light-navy: #1c2c8c;
    --light-cyan: #39d0ee;
    --light-magenta: #e0208a;
    --light-red: #f0303a;
    --light-yellow: #f6e02a;
    --light-green: #3fd46a;
    --light-violet: #8a3ad8;
  }
  html, body {
    margin: 0;
    padding: 0;
    overflow: hidden;
    background: #ffffff;
  }
  .cover {
    position: relative;
    width: 1200px;
    height: 1190px;
    overflow: hidden;
  }
  .cover-art {
    position: absolute;
    inset: 0;
    width: 1200px;
    height: 1190px;
  }
  .album-title {
    position: absolute;
    left: 590px;
    top: 470px;
    margin: 0;
    transform: translate(-50%, -50%) rotate(-14deg);
    font-family: "Titan One", sans-serif;
    font-weight: 400;
    font-size: 148px;
    line-height: 0.98;
    color: var(--title-blue);
    text-align: center;
    white-space: nowrap;
    text-shadow: 9px 9px 0 var(--title-shadow);
    letter-spacing: 1px;
  }
  .album-title .title-line {
    display: block;
  }
  .album-title .title-line--second {
    padding-left: 60px;
  }
  .track-list {
    position: absolute;
    left: 646px;
    top: 764px;
    transform: translateX(-50%);
    margin: 0;
    padding: 0;
    list-style: none;
    font-family: "Open Sans", sans-serif;
    font-weight: 700;
    font-size: 25px;
    line-height: 41px;
    color: var(--track-ink);
    text-align: center;
    white-space: nowrap;
  }
</style>
</head>
<body>
<main class="cover">
  <svg class="cover-art" viewBox="0 0 1200 1190" xmlns="http://www.w3.org/2000/svg">
    <defs>
      <linearGradient id="light-streaks" x1="0" y1="0" x2="1" y2="1">
        <stop offset="0" stop-color="var(--light-navy)"/>
        <stop offset="0.22" stop-color="var(--light-blue)"/>
        <stop offset="0.42" stop-color="var(--light-cyan)"/>
        <stop offset="0.6" stop-color="var(--light-magenta)"/>
        <stop offset="0.78" stop-color="var(--light-yellow)"/>
        <stop offset="1" stop-color="var(--light-cyan)"/>
      </linearGradient>
      <radialGradient id="light-glow" cx="0.25" cy="0.7" r="0.6">
        <stop offset="0" stop-color="var(--light-red)" stop-opacity="0.75"/>
        <stop offset="0.5" stop-color="var(--light-violet)" stop-opacity="0.35"/>
        <stop offset="1" stop-color="var(--light-violet)" stop-opacity="0"/>
      </radialGradient>
      <radialGradient id="disc-fill" cx="0.5" cy="0.55" r="0.5">
        <stop offset="0" stop-color="var(--disc-white)" stop-opacity="0.95"/>
        <stop offset="0.75" stop-color="var(--disc-white)" stop-opacity="0.82"/>
        <stop offset="1" stop-color="var(--disc-white)" stop-opacity="0.6"/>
      </radialGradient>
    </defs>
    <g role="img" aria-label="Bunte Lichtstrahlen in Blau, Türkis, Pink, Rot und Gelb, die aus der Mitte nach außen schießen">
      <rect width="1200" height="1190" fill="url(#light-streaks)"/>
      <rect width="1200" height="1190" fill="url(#light-glow)"/>
    </g>
    <g class="title-disc">
      <circle cx="646" cy="636" r="470" fill="url(#disc-fill)"/>
      <circle cx="646" cy="636" r="510" fill="none" stroke="#ffffff" stroke-opacity="0.75" stroke-width="5"/>
      <circle cx="660" cy="650" r="488" fill="none" stroke="#ffffff" stroke-opacity="0.9" stroke-width="4"/>
    </g>
  </svg>

  <h1 class="album-title" aria-label="Sommerpfauenfest">
    <span class="title-line">Sommer</span>
    <span class="title-line title-line--second">pfauenfest</span>
  </h1>

  <ul class="track-list">
    <li>u.a. Eine Rose, die nach Morgen duftet</li>
    <li>Bis zum letzten Leuchtturm&nbsp;&nbsp;Der Sommer bleibt Gold</li>
    <li>Egon, wir tanzen bis Mainz</li>
    <li>Ganz viel Sonnenschein …</li>
  </ul>
</main>
</body>
</html>
```